Business card design needed

We are a smash repair business and have been in operation for almost 10 years. We have always had a card with a solid yellow background and black car door as a logo. We don't want to stray too far from this as all of our advertising incorporates same.

We do not wish to have anything comical or too wordy.

Industry/Entity Type

Advertising

Contact Information for Business Card

Rhys & Gemma Tolland
Brookvale Ridge Panel Works
Bays 7-11 Wexford Crescent
Tarrowby NSW 2471
02 6571 3820
0428 362 057
office@brookvaleridgepanelworks.com.au

Logo Text

Brookvale Ridge Panel Works

Logo styles of interest
Emblem Logo

```html
<!DOCTYPE html>
<html lang="en">
<head>
<meta charset="utf-8">
<title>Brookvale Ridge Panel Works – Business Card</title>
<link rel="stylesheet" href="https://fonts.googleapis.com/css2?family=Noto+Sans:wght@400;500;700&display=swap">
<style>
  :root {
    --card-yellow: #f3e630;
    --card-black: #121212;
    --ink: #111111;
    --stage: #2b2622;
    --shadow: rgba(0, 0, 0, 0.45);
  }
  * { margin: 0; padding: 0; box-sizing: border-box; }
  html, body {
    width: 1200px;
    height: 1000px;
    overflow: hidden;
    background: var(--stage);
    font-family: "Noto Sans", Verdana, sans-serif;
  }
  .stage {
    position: relative;
    width: 1200px;
    height: 1000px;
  }
  .card {
    position: absolute;
    left: 320px;
    width: 560px;
    height: 340px;
    box-shadow: 0 14px 30px var(--shadow);
    overflow: hidden;
  }
  /* Front side */
  .card--front {
    top: 140px;
    background: var(--card-yellow);
    color: var(--ink);
  }
  .brand {
    position: absolute;
    top: 26px;
    left: 34px;
    display: flex;
    align-items: center;
    gap: 12px;
  }
  .brand__mark {
    width: 26px;
    height: 26px;
    background: var(--ink);
  }
  .brand__name {
    font-size: 17px;
    font-weight: 500;
    color: var(--ink);
  }
  .contact {
    position: absolute;
    left: 150px;
    top: 188px;
    line-height: 1.32;
    white-space: nowrap;
  }
  .contact__names {
    font-size: 17px;
    font-weight: 400;
    letter-spacing: 0.04em;
    text-transform: uppercase;
    margin-bottom: 2px;
  }
  .contact__line {
    font-size: 15px;
    font-weight: 500;
  }
  .contact__label {
    font-size: 11px;
    font-weight: 400;
    text-transform: uppercase;
    margin-right: 5px;
  }
  /* Back side */
  .card--back {
    top: 520px;
    background: linear-gradient(180deg, #1a1a1a 0%, var(--card-black) 100%);
  }
  .tagline-band {
    position: absolute;
    top: 0;
    right: 0;
    width: 156px;
    height: 100%;
    background: var(--card-yellow);
    color: var(--ink);
  }
  .tagline {
    position: absolute;
    left: 22px;
    bottom: 36px;
    font-size: 15px;
    line-height: 1.2;
  }
  .tagline__lead { font-weight: 700; display: block; }
  .tagline__rest { display: block; padding-left: 12px; }
</style>
</head>
<body>
  <main class="stage">
    <section class="card card--front" aria-label="Business card front">
      <div class="brand">
        <span class="brand__mark"></span>
        <span class="brand__name">Brookvale Ridge Panel Works</span>
      </div>
      <div class="contact">
        <p class="contact__names">Rhys &amp; Gemma Tolland</p>
        <p class="contact__line">Brookvale Ridge Panel Works Bays 7-11</p>
        <p class="contact__line">Wexford Crescent Tarrowby NSW 2471</p>
        <p class="contact__line"><span class="contact__label">Phone</span>02 6571 3820 0428 362 057</p>
        <p class="contact__line"><span class="contact__label">Email</span>office@brookvaleridgepanelworks.com.au</p>
      </div>
    </section>

    <section class="card card--back" aria-label="Business card back">
      <div class="tagline-band">
        <p class="tagline">
          <span class="tagline__lead">AUTO</span>
          <span class="tagline__rest">collision</span>
          <span class="tagline__rest">repair</span>
        </p>
      </div>
    </section>
  </main>
</body>
</html>
```